Glossaro: Graphic elements & webpage layout

Hi there! We’re building a site called Glossaro.com—it will be a community site for beauty product reviews, product recommendations and beauty tutorials. We've already got a logo, thanks to another ArtHively project. This project on ArtHively involves the following web design work:

1) Propose the overall graphic design elements of our site (according to our guidelines, which are in the attached file)

-Color Palette
-Fonts
-Icon set(s)

2) Using the overall graphic design elements in step 1 and our storyboard (attached), develop a webpage layout for the "How-to" page of our site. The "How-to" pages will be an editorial format, where our beauty journalist will show a video (and photos) of step-by-step beauty tutorials.

Please take a look at the attached files for a detailed brief and the logo! Thanks and we're looking forward to working with you!

Target Market(s)

Glossaro is for a French, English, and American audience of women between the ages of 16 and 30, who buy and use beauty products regularly.

Industry/Entity Type

Graphic Design

Requirements
Must have
• 1) A global set of graphic standards for the website Glossaro.com:
• A color palette
• Fonts
• An icon set (or sets)
• A menu
• Other graphic elements like button styles

2) A webpage layout (non-coded) for the How-To page template
(See storyboard, attached separately)
This webpage layout is for the main editorial format on Glossaro—step by step beauty tutorials. The individual on-page elements are in the storyboard, but overall we’d like it to look clean, friendly, and to encourage community participation and sharing on social networks.
Nice to have
• • A look and feel that is fresh, clean and modern
• Proximity: Establishes a close proximity with the user. (We want them to get the same feeling they get when talking beauty tips with their close friends).
• Neutrality: A sincere and neutral look and feel that doesn’t suggest a preference for any particular or elite type of beauty (but it can still be fun!)
• The graphic design is relevant to the beauty sector as a whole. (We could be talking about lipstick, a hairbrush or a man’s cologne)
• The graphic design alludes to the beauty industry (discreetly, not overtly!)
Should not have
• We've already got a logo, so you shouldn't suggest a new one!

We really want to avoid designs that are too traditionally "beauty" or too girly and feminine. Please no pink, no flowers, etc! :)

```html
<!DOCTYPE html>
<html lang="fr">
<head>
<meta charset="utf-8">
<title>Glossaro – Tutorial</title>
<link href="https://fonts.googleapis.com/css2?family=Questrial&family=Arimo:wght@400;700&display=swap" rel="stylesheet">
<style>
:root{
  --page:#f4f4f4;
  --panel:#efefef;
  --bar:#3b3b3b;
  --teal:#13c6b3;
  --mint:#0edc9f;
  --orange:#f2861a;
  --ink:#2b2b2b;
  --muted:#555;
  --field:#fcebcc;
  --field-line:#e9b566;
  --star:#f5a516;
  --share-dark:#2c62a8;
  --share-light:#4fb1e0;
}
*{box-sizing:border-box;margin:0;padding:0}
html,body{width:1200px;height:2200px;overflow:hidden}
body{position:relative;background:var(--page);font-family:"Arimo",Arial,sans-serif;color:var(--ink)}
.abs{position:absolute}

.topbar{left:0;top:0;width:1200px;height:34px;background:var(--bar)}
.lang-link{left:866px;top:9px;font-size:13px;color:var(--teal)}
.social-mini{top:4px;width:24px;height:24px;border-radius:5px;background:var(--share-light)}

.content-panel{left:122px;top:95px;width:959px;height:2010px;background:var(--panel)}

.brand{left:125px;top:54px;font-family:"Questrial",sans-serif;font-size:58px;color:var(--ink);letter-spacing:-1px}
.nav-btn{top:84px;height:30px;width:88px;background:linear-gradient(#8a8a8a,#5e5e5e);color:#fff;font-size:13px;text-align:center;line-height:30px;border-radius:2px;box-shadow:0 1px 2px rgba(0,0,0,.4)}
.search{left:893px;top:82px;width:181px;height:33px;background:linear-gradient(#d6d6d6,#bdbdbd);border-radius:3px;font-size:11px;color:#999;padding:10px 12px}
.search svg{position:absolute;right:9px;top:6px}

.title{left:126px;top:176px;font-family:"Questrial",sans-serif;font-weight:400;font-size:23px;color:#444;letter-spacing:.5px}
.share{top:168px;width:36px;height:36px;border-radius:50%}
.share.dark{left:513px;background:var(--share-dark)}
.share.light{left:566px;background:var(--share-light)}
.like{left:623px;top:166px;width:48px;height:38px;border:2px solid #777;border-radius:3px;background:#fff}
.meta{top:230px;font-family:"Questrial",sans-serif;font-size:17px;color:#333}
.stars{left:206px;top:222px}

.frame{background:var(--teal)}
.video{background:#000}
.controls{background:#f1f1f1;border-top:2px solid #e33}
.play{position:absolute}

.products{background:var(--mint)}
.products h2{position:absolute;left:18px;top:12px;font-family:"Questrial",sans-serif;font-weight:400;font-size:20px;color:#123}
.need-list{position:absolute;left:18px;top:52px;list-style:none;font-family:"Questrial",sans-serif;font-size:14px;color:#123}
.need-list li{height:23.5px;padding-left:16px;position:relative}
.need-list li::before{content:"";position:absolute;left:1px;top:4px;width:6px;height:6px;border-right:2px solid #123;border-top:2px solid #123;transform:rotate(45deg)}

.card{position:absolute;width:170px;height:80px}
.thumb{position:absolute;left:0;top:0;width:72px;height:79px}
.t1{background:linear-gradient(135deg,#f1d6c6,#8a5a48)}
.t2{background:linear-gradient(135deg,#f6f4ee,#9dcf8e)}
.t3{background:linear-gradient(135deg,#e8c7a6,#6b4430)}
.t4{background:linear-gradient(135deg,#e33a2c,#1e1a16)}
.card .name{position:absolute;left:80px;top:0;font-family:"Questrial",sans-serif;font-weight:700;font-size:14px;color:#1c1c1c}
.card .info{position:absolute;left:80px;top:17px;font-family:"Questrial",sans-serif;font-size:13px;line-height:15px;color:#fff}
.card .bag{position:absolute;left:80px;top:52px;width:22px;height:26px;background:#274a44;border-radius:2px}

.body-text{width:545px;font-size:13px;line-height:20px;text-align:justify;color:#222}

.step-btn{height:38px;background:linear-gradient(#f4f4f4,#d3d3d3);border:1px solid #b4b4b4;border-radius:2px;font-family:"Questrial",sans-serif;font-size:18px;color:#333;padding:9px 10px}
.tab{height:38px;width:104px;font-family:"Questrial",sans-serif;font-size:18px;color:#fff;text-align:center;line-height:38px;border-radius:2px 2px 0 0}
.tab.on{background:var(--orange)}
.tab.off{background:var(--mint);color:#134}

.slide{background:linear-gradient(160deg,#f7ece4,#e8a27a 55%,#f4e6db)}
.arrow{width:40px;height:40px;border-radius:50%;background:#111}
.arrow svg{display:block}

.label{font-family:"Questrial",sans-serif;font-size:15px;color:#222}
.field{background:var(--field);border:1px solid var(--field-line);border-radius:4px}
.placeholder{font-size:11px;color:#222;padding:8px}
.submit{left:515px;top:1926px;width:155px;height:41px;background:linear-gradient(#8c8c8c,#5f5f5f);color:#fff;font-family:"Questrial",sans-serif;font-size:22px;text-align:center;line-height:41px;border-radius:3px;border:1px solid #444}
.comment{left:125px;top:1979px;width:545px;height:119px;padding:12px 8px;font-size:11px;line-height:14px;letter-spacing:.5px}

.footer{left:0;top:2105px;width:1200px;height:95px;background:var(--bar)}
.footer-brand{left:128px;top:2120px;font-family:"Questrial",sans-serif;font-size:40px;color:#6f6f6f}
.copyright{left:883px;top:2140px;font-size:12px;letter-spacing:.8px;color:var(--teal)}
</style>
</head>
<body>

<header>
  <div class="abs topbar"></div>
  <span class="abs lang-link">Choix de la langue</span>
  <span class="abs social-mini" style="left:1006px" aria-label="Réseau social"></span>
  <span class="abs social-mini" style="left:1048px;background:#3e64a6" aria-label="Réseau social"></span>
</header>

<div class="abs content-panel"></div>

<div class="abs brand">Glossaro</div>
<nav>
  <div class="abs nav-btn" style="left:663px">HOW TO</div>
  <div class="abs nav-btn" style="left:767px">TIPS</div>
</nav>
<div class="abs search">search
  <svg width="22" height="22" viewBox="0 0 22 22"><circle cx="8" cy="8" r="6" fill="none" stroke="#111" stroke-width="3"/><line x1="12" y1="12" x2="20" y2="20" stroke="#111" stroke-width="4"/></svg>
</div>

<h1 class="abs title">TITRE DU TUTORIAL</h1>
<span class="abs share dark" aria-label="Partager"></span>
<span class="abs share light" aria-label="Partager"></span>
<span class="abs like">
  <svg width="44" height="34" viewBox="0 0 44 34"><path d="M13 15h5l6-9c2 0 3 2 2 5l-1 4h8c2 0 3 2 2 4l-3 9c-1 2-2 2-4 2H18V15z" fill="#18b5a6"/><rect x="11" y="15" width="5" height="14" fill="#18b5a6"/></svg>
</span>

<div class="abs meta" style="left:126px">Difficulté:</div>
<svg class="abs stars" width="96" height="28" viewBox="0 0 96 28">
  <g fill="var(--star)" stroke="#c27a05" stroke-width="1">
    <polygon points="14,2 17.5,10 26,10.5 19.5,16 21.5,25 14,20 6.5,25 8.5,16 2,10.5 10.5,10"/>
    <polygon transform="translate(31 0)" points="14,2 17.5,10 26,10.5 19.5,16 21.5,25 14,20 6.5,25 8.5,16 2,10.5 10.5,10"/>
    <polygon transform="translate(62 0)" points="14,2 17.5,10 26,10.5 19.5,16 21.5,25 14,20 6.5,25 8.5,16 2,10.5 10.5,10"/>
  </g>
</svg>
<div class="abs meta" style="left:333px">Durée: 20 minutes</div>
<div class="abs meta" style="left:513px">Occasion: Soirée</div>

<!-- Intro video -->
<div class="abs frame" style="left:125px;top:264px;width:545px;height:308px"></div>
<div class="abs video" role="img" aria-label="Video of the tutorial" style="left:134px;top:272px;width:527px;height:270px"></div>
<svg class="play" style="left:372px;top:352px" width="60" height="76" viewBox="0 0 60 76"><polygon points="4,2 58,38 4,74" fill="#eee"/></svg>
<div class="abs controls" style="left:134px;top:542px;width:527px;height:22px"></div>

<aside class="abs products" style="left:704px;top:264px;width:371px;height:308px">
  <h2>Les produits nécessaires</h2>
  <ul class="need-list"><li>Produit 1</li><li>Produit 2</li><li>Produit 3</li></ul>
</aside>

<p class="abs body-text" style="left:125px;top:589px">Lorem ipsum dolor sit amet, maiores ornare ac fermentum, imperdiet ut vivamus a, nam lectus at nunc. Quam euismod sem, semper ut potenti pellentesque quisque. In eget sapien sed, sit duis vestibulum ultricies, placerat morbi amet vel, nullam in in lorem vel.</p>

<!-- Step 1 -->
<div class="abs step-btn" style="left:125px;top:685px;width:110px">ETAPE 1</div>
<div class="abs tab on" style="left:126px;top:738px">Vidéo</div>
<div class="abs tab off" style="left:233px;top:738px">Photos</div>
<div class="abs frame" style="left:125px;top:773px;width:545px;height:308px"></div>
<div class="abs video" role="img" aria-label="Video of step 1" style="left:134px;top:781px;width:527px;height:270px"></div>
<svg class="play" style="left:372px;top:861px" width="60" height="76" viewBox="0 0 60 76"><polygon points="4,2 58,38 4,74" fill="#eee"/></svg>
<div class="abs controls" style="left:134px;top:1051px;width:527px;height:22px"></div>

<aside class="abs products" style="left:704px;top:773px;width:371px;height:310px">
  <div class="card" style="left:16px;top:16px"><div class="thumb t1" role="img" aria-label="Product photo"></div><span class="name">Produit 1</span><span class="info">Marque<br>Prix</span><span class="bag"></span></div>
  <div class="card" style="left:191px;top:16px"><div class="thumb t2" role="img" aria-label="Product photo"></div><span class="name">Produit 1</span><span class="info">Marque<br>Prix</span><span class="bag"></span></div>
  <div class="card" style="left:16px;top:112px"><div class="thumb t3" role="img" aria-label="Product photo"></div><span class="name">Produit 1</span><span class="info">Marque<br>Prix</span><span class="bag"></span></div>
  <div class="card" style="left:191px;top:112px"><div class="thumb t4" role="img" aria-label="Product photo"></div><span class="name">Produit 1</span><span class="info">Marque<br>Prix</span><span class="bag"></span></div>
  <div class="card" style="left:16px;top:207px"><div class="thumb t1" role="img" aria-label="Product photo"></div><span class="name">Produit 1</span><span class="info">Marque<br>Prix</span><span class="bag"></span></div>
  <div class="card" style="left:191px;top:207px"><div class="thumb t2" role="img" aria-label="Product photo"></div><span class="name">Produit 1</span><span class="info">Marque<br>Prix</span><span class="bag"></span></div>
</aside>

<p class="abs body-text" style="left:125px;top:1099px">Lorem ipsum dolor sit amet, maiores ornare ac fermentum, imperdiet ut vivamus a, nam lectus at nunc. Quam euismod sem, semper ut potenti pellentesque quisque. In eget sapien sed, sit duis vestibulum ultricies, placerat morbi amet vel, nullam in in lorem vel.</p>

<!-- Step 2 -->
<div class="abs step-btn" style="left:125px;top:1200px;width:110px">ETAPE 2</div>
<div class="abs tab off" style="left:126px;top:1251px">Vidéo</div>
<div class="abs tab on" style="left:233px;top:1251px">Photos</div>
<div class="abs frame" style="left:125px;top:1288px;width:545px;height:308px"></div>
<div class="abs slide" role="img" aria-label="Photo of step 2" style="left:194px;top:1320px;width:405px;height:238px"></div>
<div class="abs arrow" style="left:146px;top:1425px"><svg width="40" height="40" viewBox="0 0 40 40"><polyline points="23,12 15,20 23,28" fill="none" stroke="#fff" stroke-width="4"/></svg></div>
<div class="abs arrow" style="left:607px;top:1425px"><svg width="40" height="40" viewBox="0 0 40 40"><polyline points="17,12 25,20 17,28" fill="none" stroke="#fff" stroke-width="4"/></svg></div>

<aside class="abs products" style="left:704px;top:1289px;width:371px;height:213px">
  <div class="card" style="left:16px;top:17px"><div class="thumb t1" role="img" aria-label="Product photo"></div><span class="name">Produit 1</span><span class="info">Marque<br>Prix</span><span class="bag"></span></div>
  <div class="card" style="left:191px;top:17px"><div class="thumb t2" role="img" aria-label="Product photo"></div><span class="name">Produit 1</span><span class="info">Marque<br>Prix</span><span class="bag"></span></div>
  <div class="card" style="left:16px;top:112px"><div class="thumb t3" role="img" aria-label="Product photo"></div><span class="name">Produit 1</span><span class="info">Marque<br>Prix</span><span class="bag"></span></div>
  <div class="card" style="left:191px;top:112px"><div class="thumb t4" role="img" aria-label="Product photo"></div><span class="name">Produit 1</span><span class="info">Marque<br>Prix</span><span class="bag"></span></div>
</aside>

<p class="abs body-text" style="left:125px;top:1614px">Lorem ipsum dolor sit amet, maiores ornare ac fermentum, imperdiet ut vivamus a, nam lectus at nunc. Quam euismod sem, semper ut potenti pellentesque quisque. In eget sapien sed, sit duis vestibulum ultricies, placerat morbi amet vel, nullam in in lorem vel.</p>

<!-- Comments -->
<div class="abs step-btn" style="left:126px;top:1715px;width:219px;height:43px;padding:12px 13px">COMMENTAIRES (12)</div>
<span class="abs label" style="left:129px;top:1779px">Nom</span>
<div class="abs field" style="left:307px;top:1772px;width:363px;height:34px"></div>
<span class="abs label" style="left:127px;top:1826px;font-size:14px">Mail (n'apparaitra pas)</span>
<div class="abs field" style="left:307px;top:1818px;width:363px;height:33px"></div>
<div class="abs field placeholder" style="left:126px;top:1865px;width:544px;height:47px">Laissez votre commentaire ici !</div>
<div class="abs submit">Commenter</div>
<div class="abs field comment">Lorem ipsum dolor sit amet, maiores ornare ac fermentum, imperdiet ut vivamus a, nam lectus at nunc. Quam euismod sem, semper ut potenti pellentesque quisque. In eget sapien sed, sit duis vestibulum ultricies, placerat morbi amet vel, nullam in in lorem vel.<br><br>Commentaire de [nom] posté le [date]</div>

<footer>
  <div class="abs footer"></div>
  <div class="abs footer-brand">Glossaro</div>
  <div class="abs copyright">Copyright © glossaro.com 2011</div>
</footer>

</body>
</html>
```